Brindle Yard brochure to showcase Masonry, landscape and concrete services

SEE RECENT COMMENT PAGE FOR BEST INFO We need a brochure designed to help inform our clients of our services and give them information on the pitfalls in the masonry, landscape and Hardscape industry, including drainage and frost protection, showcase some of our work we like to make all our material for marketing geared toward helping the client learn something. Drainage on any site is the number one component to a successful landscape, Hardscape and outdoor living area. This is often and overlooked to get to the stuff that's fun in turn, causing failure from frost due to northern Minnesota's harsh climate. Creating many disappointments on a large investment project. The brochure should also have a section focused on masonry, including fireplaces chimney repair, stucco repair, stone and brick. Some of the language should be editable. I will attach pictures and our logo.

Target Market(s)

Older customers with dual income looking to update and add outdoor living

Industry/Entity Type

Masonry, landscape, concrete, outdoor living

Font styles to use
Serif
Sans Serif
Other font styles liked:
• Arial

Colors

Designer to choose only greyscale colors for use in the design.

Requirements
Must have
• I really like gray, silver and black when I do marketing mixed with White, but I thought adding some greenery for the landscape portion might look good too on this brochure
Nice to have
• I do not like it too busy so keep it clean and simple
Should not have
• Tons of clutter, tons of words, hard to read and look at

```html
<!DOCTYPE html>
<html lang="en">
<head>
<meta charset="utf-8">
<title>Brindle Yard Trifold Brochure</title>
<link href="https://fonts.googleapis.com/css2?family=Archivo+Black&family=Arimo:ital,wght@0,400;0,700;1,400&display=swap" rel="stylesheet">
<style>
  :root{
    --backdrop:#6b6b6e;
    --paper:#f2f2f0;
    --ink:#1e1e1e;
    --body:#4a4a4a;
    --muted:#a3a3a3;
    --green:#4caf50;
    --green-soft:#a8d8a6;
    --dark-panel:#2f2f31;
    --fold:rgba(0,0,0,.07);
  }
  *{box-sizing:border-box;margin:0;padding:0}
  html,body{width:1200px;height:2700px;overflow:hidden}
  body{background:var(--backdrop);font-family:"Arimo",Arial,sans-serif;color:var(--body);position:relative}
  .spread{position:absolute;left:50px;width:1100px;height:850px;background:var(--paper);box-shadow:0 18px 40px rgba(0,0,0,.35);overflow:hidden}
  .spread--outside{top:250px}
  .spread--inside{top:1400px}
  .spread svg.art{position:absolute;inset:0;width:1100px;height:850px}
  .fold{position:absolute;top:0;bottom:0;width:2px;background:var(--fold)}
  .panel{position:absolute;top:0;width:366px;height:850px}
  .p1{left:0}.p2{left:367px}.p3{left:734px}
  .heading{font-family:"Archivo Black","Arial Black",sans-serif;color:var(--ink);line-height:1.15;font-weight:400}
  .heading .soft{color:var(--muted)}
  .rule{width:70px;height:2px;background:var(--green);margin:12px 0 14px}
  p{font-size:14px;line-height:1.55}
  /* outside */
  .who{position:absolute;left:40px;top:60px;width:290px}
  .who .heading{font-size:26px}
  .who p+p{margin-top:14px}
  .cta{position:absolute;left:30px;top:560px;width:306px;text-align:center}
  .cta .heading{font-size:22px}
  .cta .lead{font-size:13px;margin:8px 0 20px}
  .contact-label{font-weight:700;color:var(--ink);font-size:14px}
  .contact-value{font-size:14px;margin-bottom:12px}
  .cover{position:absolute;left:40px;top:490px;width:290px}
  .brand{display:flex;align-items:center;gap:10px;margin-bottom:22px}
  .brand-dot{width:26px;height:26px;border-radius:50%;background:var(--muted)}
  .brand-name{font-size:16px;font-weight:700;letter-spacing:3px;color:var(--muted)}
  .brand-tag{font-size:10px;color:var(--muted);margin-top:2px;letter-spacing:1px}
  .cover .heading{font-size:30px}
  .cover .sub{font-size:14px;font-style:italic}
  /* inside */
  .foundation{position:absolute;left:36px;top:420px;width:300px}
  .foundation .heading{font-size:23px}
  .steps{list-style:none;margin-top:10px}
  .step{display:flex;gap:12px;align-items:flex-start;margin-bottom:16px}
  .step-num{flex:0 0 34px;height:34px;border-radius:50%;background:#7a7a7a;color:#fff;font-size:12px;font-weight:700;display:flex;align-items:center;justify-content:center}
  .step-num--active{background:var(--green)}
  .step p{font-size:12.5px;line-height:1.45}
  .p2.dark{background:var(--dark-panel)}
  .services{position:absolute;left:30px;top:50px;width:306px;text-align:center}
  .services .heading{color:#fff;font-size:21px}
  .services .rule{margin:12px auto 22px}
  .service{margin-bottom:20px}
  .service-photo{width:130px;height:84px;border-radius:12px;margin:0 auto 8px;border:2px solid #fff}
  .service p{color:#d6d6d6;font-size:12px;line-height:1.4}
  .masonry{position:absolute;left:40px;top:60px;width:290px}
  .masonry .heading{font-size:23px}
  .bullets{list-style:none}
  .bullets li{font-size:13.5px;line-height:1.45;padding-left:18px;position:relative;margin-bottom:9px}
  .bullets li::before{content:"";position:absolute;left:0;top:6px;width:7px;height:7px;background:var(--green)}
</style>
</head>
<body>

<section class="spread spread--outside" aria-label="Brochure outside spread">
  <svg class="art" viewBox="0 0 1100 850" aria-hidden="false">
    <defs>
      <linearGradient id="house" x1="0" y1="0" x2="1" y2="1">
        <stop offset="0" stop-color="#4d5256"/><stop offset=".5" stop-color="#7e9bb0"/><stop offset="1" stop-color="#5b6a47"/>
      </linearGradient>
      <linearGradient id="slope" x1="0" y1="0" x2="1" y2="1">
        <stop offset="0" stop-color="#6b7a45"/><stop offset="1" stop-color="#5a4638"/>
      </linearGradient>
      <linearGradient id="greenview" x1="0" y1="0" x2="1" y2="1">
        <stop offset="0" stop-color="#8fcf7e"/><stop offset="1" stop-color="#4f8f3c"/>
      </linearGradient>
    </defs>
    <path role="img" aria-label="Photo of a modern home with large windows over a stone foundation and garden"
      fill="url(#house)"
      d="M367,0 H1100 V330 C1080,420 990,445 930,430 C880,418 855,395 830,360 C800,318 760,300 733,300 C733,450 650,520 550,520 C450,520 367,440 367,330 Z"/>
    <circle cx="826" cy="360" r="50" fill="#fff"/>
    <circle cx="826" cy="360" r="42" fill="var(--green-soft)"/>
    <path role="img" aria-label="Photo of a rocky landscaped slope with native plantings"
      fill="url(#slope)"
      d="M0,850 V650 C50,590 140,570 200,610 C250,645 310,610 367,570 V850 Z"/>
    <circle cx="292" cy="660" r="56" fill="#fff"/>
    <circle role="img" aria-label="Photo of an outdoor kitchen on a patio" cx="292" cy="660" r="49" fill="url(#greenview)"/>
  </svg>
  <div class="fold" style="left:366px"></div>
  <div class="fold" style="left:733px"></div>

  <div class="panel p1">
    <div class="who">
      <h2 class="heading"><span class="soft">Who</span> We Are</h2>
      <div class="rule"></div>
      <p>Brindle Yard is a trusted masonry and landscape company serving northern Minnesota and Wisconsin. By focusing on smart planning and client education, we help ensure every project meets expectations.</p>
      <p>In our harsh climate, proper drainage, frost protection, and water management are essential to safeguard outdoor investments. Specializing in masonry, landscaping, and outdoor living spaces, Brindle Yard combines natural beauty with lasting craftsmanship.</p>
    </div>
  </div>

  <div class="panel p2">
    <div class="cta">
      <h2 class="heading">Ready to Create Your Dream <span class="soft">Outdoor Space?</span></h2>
      <p class="lead">Call us today to schedule a consultation!</p>
      <div class="contact-label">Phone:</div>
      <div class="contact-value">XXX-XXX-XXXX</div>
      <div class="contact-label">Email Address:</div>
      <div class="contact-value">info@yourcompany.com</div>
      <div class="contact-label">Website</div>
      <div class="contact-value">www.yourcompany.com</div>
    </div>
  </div>

  <div class="panel p3">
    <div class="cover">
      <div class="brand">
        <span class="brand-dot"></span>
        <div>
          <div class="brand-name">BRINDLE YARD</div>
          <div class="brand-tag">Masonry &amp; Landscape</div>
        </div>
      </div>
      <h1 class="heading">Enhance Your <span class="soft">Outdoor</span> Living with Confidence</h1>
      <div class="rule"></div>
      <p class="sub">Expert Masonry, Landscaping &amp; Hardscape Solutions for Lasting Beauty</p>
    </div>
  </div>
</section>

<section class="spread spread--inside" aria-label="Brochure inside spread">
  <svg class="art" viewBox="0 0 1100 850">
    <defs>
      <linearGradient id="kitchen" x1="0" y1="0" x2="1" y2="1">
        <stop offset="0" stop-color="#5f7a3e"/><stop offset=".55" stop-color="#a89b86"/><stop offset="1" stop-color="#6e6a63"/>
      </linearGradient>
      <linearGradient id="grill" x1="0" y1="0" x2="1" y2="1">
        <stop offset="0" stop-color="#9a9a9a"/><stop offset="1" stop-color="#4a4a4a"/>
      </linearGradient>
      <linearGradient id="hillside" x1="0" y1="0" x2="1" y2="1">
        <stop offset="0" stop-color="#c9b8a4"/><stop offset=".5" stop-color="#6f7c4a"/><stop offset="1" stop-color="#6a4a3a"/>
      </linearGradient>
      <linearGradient id="pavilion" x1="0" y1="0" x2="1" y2="1">
        <stop offset="0" stop-color="#8fcf7e"/><stop offset="1" stop-color="#3f6f3a"/>
      </linearGradient>
    </defs>
    <path role="img" aria-label="Photo of an outdoor kitchen with grill and stone counters on a patio"
      fill="url(#kitchen)"
      d="M0,0 H367 V290 C330,300 300,320 280,345 C240,395 170,390 120,360 C70,330 30,330 0,345 Z"/>
    <circle cx="255" cy="330" r="58" fill="#fff"/>
    <circle role="img" aria-label="Close-up photo of a built-in grill" cx="255" cy="330" r="51" fill="url(#grill)"/>

    <circle cx="920" cy="560" r="120" fill="none" stroke="#e4e4e2" stroke-width="14"/>

    <path role="img" aria-label="Photo of a hillside stone path leading to a glass pavilion at sunset"
      fill="url(#hillside)"
      d="M734,850 V600 C780,560 840,560 880,600 C920,640 1000,630 1100,560 V850 Z"/>
    <circle cx="860" cy="640" r="58" fill="#fff"/>
    <circle role="img" aria-label="Photo of a glass pavilion among greenery" cx="860" cy="640" r="51" fill="url(#pavilion)"/>
    <path d="M1100,790 V850 H1030 Z" fill="var(--green)"/>
  </svg>
  <div class="fold" style="left:733px"></div>

  <div class="panel p1">
    <div class="foundation">
      <h2 class="heading">The <span class="soft">Foundation</span> of a Successful Outdoor Project</h2>
      <div class="rule"></div>
      <ol class="steps">
        <li class="step"><span class="step-num step-num--active">01</span><p>Drainage is the number one component of any outdoor space. Without it, even the most beautiful design can fail.</p></li>
        <li class="step"><span class="step-num">02</span><p>Harsh northern Minnesota winters make frost a serious threat, causing cracks &amp; structural damage if drainage is ignored.</p></li>
        <li class="step"><span class="step-num">03</span><p>Proper planning prevents disappointments and protects your investment.</p></li>
      </ol>
    </div>
  </div>

  <div class="panel p2 dark">
    <div class="services">
      <h2 class="heading">Transform Your Outdoors with Expertise</h2>
      <div class="rule"></div>
      <div class="service">
        <div class="service-photo" role="img" aria-label="Photo of a landscaped backyard" style="background:linear-gradient(135deg,#6c7d58,#9aa3a6)"></div>
        <p>Full landscaping design &amp; installation</p>
      </div>
      <div class="service">
        <div class="service-photo" role="img" aria-label="Photo of a stone patio with fireplace" style="background:linear-gradient(135deg,#8a6a4e,#c9a27c)"></div>
        <p>Hardscape solutions: patios, walkways, retaining walls</p>
      </div>
      <div class="service">
        <div class="service-photo" role="img" aria-label="Photo of an outdoor kitchen" style="background:linear-gradient(135deg,#7a8c5a,#b2aca0)"></div>
        <p>Outdoor living areas tailored for style and functionality</p>
      </div>
      <div class="service">
        <div class="service-photo" role="img" aria-label="Photo of a natural stone hillside" style="background:linear-gradient(135deg,#6e5a4a,#8a8f70)"></div>
        <p>Use of premium materials and sustainable practices</p>
      </div>
    </div>
  </div>

  <div class="panel p3">
    <div class="masonry">
      <h2 class="heading"><span class="soft">Masonry</span> Done Right – Built to Last</h2>
      <div class="rule"></div>
      <ul class="bullets">
        <li>Fireplaces &amp; chimneys</li>
        <li>Stucco repair</li>
        <li>Stone &amp; brick work</li>
        <li>Quality craftsmanship ensures beauty and durability</li>
      </ul>
    </div>
  </div>
</section>

</body>
</html>
```